vexlo-compatible banner ad set and associated landing page design

This is the message that the banner should communicate:
"Get Paid to Save the Planet - Solar Pays You Up to $750+ Every Year for Use of Your Roof"
BANNER SIZE:  300x250 would be great. (After choosing the winner, we will pay additional money to create new versions indifferent sizes as a follow-on work.)
BANNER FORMAT:  Could be an animated GIF, static JPG HTML 5, video, your call.
As for design guidelines for the ad and landing page, follow design guidance at: http://qe-tx47.leadvorn.com/rs/pivotrally/images/10%20blunders%20layout_final%20(1).pdf
The banner ad will be used on the Vexlo Ad network and should have a call to action to get the user to click to the landing page. The call to action can be two buttons within the banner ad:
"I Care About Planet Earth"
"Don't Care"
Clicking anywhere on the banner ad will drive traffic to the landing page.
On the landing page, we want a design that we can implement in pagemorrel.com to capture the following information:
- Street Number and Street Name of My Home
- My Zip Code
- Name of My Electric Utility
- My Typical Monthly Electric Bill Amount is:
- How Much I'd Like to Earn From Solar Per-Year?
After the user fills out the above, the following questions drop down:
First Name
Last Name
Email Address
Phone Number
At the end of the data entry portion of the landing page, there should be a "call to action" button.
LANDING PAGE FORMAT:  Photoshop or jpg format or html5 format would be great.

Updates
Target Market(s)
home owners
Industry/Entity Type
Home Improvement
Requirements
Nice to have
- Follow design guidance at: http://qe-tx47.leadvorn.com/rs/pivotrally/images/10%20blunders%20layout_final%20(1).pdf

```html
<!DOCTYPE html>
<html lang="en">
<head>
<meta charset="utf-8">
<title>Solar Banner Ad Set</title>
<link rel="stylesheet" href="https://fonts.googleapis.com/css2?family=Fredoka:wght@500;600;700&family=Noto+Serif:wght@700&display=swap">
<style>
  :root {
    --page-bg: #ffffff;
    --navy: #03336a;
    --ribbon: #1f6fd9;
    --ribbon-shadow: #06244d;
    --white: #ffffff;
    --cta-yellow: #fcc865;
    --cta-yellow-text: #0b2e62;
    --cta-blue: #1496f0;
    --frame: #1a1a1a;
  }
  * { box-sizing: border-box; margin: 0; padding: 0; }
  html, body {
    width: 1200px;
    height: 1200px;
    overflow: hidden;
    background: var(--page-bg);
  }
  .ad-set { position: relative; width: 1200px; height: 1200px; }
  .banner-slot {
    position: absolute;
    left: 326px;
    width: 300px;
    height: 250px;
    transform: scale(1.752);
    transform-origin: 0 0;
  }
  .banner-slot--info { top: 100px; }
  .banner-slot--cta { top: 660px; }
  .banner {
    position: relative;
    width: 300px;
    height: 250px;
    background: var(--navy);
    border: 1px solid var(--frame);
    overflow: hidden;
    font-family: "Fredoka", "Trebuchet MS", sans-serif;
    color: var(--white);
  }
  .ribbon { position: absolute; left: 0; top: 0; width: 150px; height: 145px; }
  .ribbon__kicker {
    position: absolute; left: 17px; top: 11px;
    font-size: 12.5px; font-weight: 600; letter-spacing: 0.1px;
  }
  .ribbon__upto {
    position: absolute; right: 172px; top: 32px;
    font-size: 25px; font-weight: 700; line-height: 1;
  }
  .ribbon__amount {
    position: absolute; left: 19px; top: 58px;
    font-size: 40px; font-weight: 700; line-height: 1;
  }
  .headline { position: absolute; right: 14px; top: 0; text-align: right; line-height: 1; }
  .headline__lead { position: absolute; right: 0; top: 20px; white-space: nowrap; font-size: 18px; font-weight: 600; }
  .headline__save { position: absolute; right: 4px; top: 34px; font-size: 52px; font-weight: 700; letter-spacing: 0.5px; }
  .headline__the { position: absolute; right: 20px; top: 78px; font-size: 23px; font-weight: 600; }
  .headline__planet { position: absolute; right: 6px; top: 98px; font-size: 35px; font-weight: 700; }
  .offer {
    position: absolute; left: 0; right: 0; top: 152px;
    text-align: center; font-size: 26px; font-weight: 600; line-height: 38px;
  }
  .cta {
    position: absolute; left: 50%; transform: translateX(-50%);
    border-radius: 8px; text-align: center; white-space: nowrap;
    font-family: "Noto Serif", Georgia, serif; font-weight: 700;
  }
  .cta--care {
    top: 152px; width: 254px; height: 32px; line-height: 32px;
    background: var(--cta-yellow); color: var(--cta-yellow-text); font-size: 17px;
  }
  .cta--skip {
    top: 197px; width: 112px; height: 33px; line-height: 33px;
    background: var(--cta-blue); color: var(--white); font-size: 17px;
  }
</style>
</head>
<body>
<main class="ad-set">

  <div class="banner-slot banner-slot--info">
    <section class="banner">
      <svg class="ribbon" viewBox="0 0 150 145" aria-hidden="true">
        <polygon points="12,0 147,0 147,114 79,140 12,114" fill="var(--ribbon-shadow)"/>
        <polygon points="5,0 140,0 140,108 72,133 5,108" fill="var(--ribbon)"/>
        <path d="M11,0 V104 L72,127 L134,104 V0" fill="none" stroke="var(--white)" stroke-width="1" stroke-dasharray="4 3"/>
      </svg>
      <p class="ribbon__kicker">Solar Pays You</p>
      <p class="ribbon__upto">UPTO</p>
      <p class="ribbon__amount">$750</p>
      <h2 class="headline">
        <span class="headline__lead">Get Paid to</span>
        <span class="headline__save">Save</span>
        <span class="headline__the">the</span>
        <span class="headline__planet">Planet</span>
      </h2>
      <p class="offer">+ Every Year for<br>Use of Your Roof</p>
    </section>
  </div>

  <div class="banner-slot banner-slot--cta">
    <section class="banner">
      <svg class="ribbon" viewBox="0 0 150 145" aria-hidden="true">
        <polygon points="12,0 147,0 147,114 79,140 12,114" fill="var(--ribbon-shadow)"/>
        <polygon points="5,0 140,0 140,108 72,133 5,108" fill="var(--ribbon)"/>
        <path d="M11,0 V104 L72,127 L134,104 V0" fill="none" stroke="var(--white)" stroke-width="1" stroke-dasharray="4 3"/>
      </svg>
      <p class="ribbon__kicker">Solar Pays You</p>
      <p class="ribbon__upto">UPTO</p>
      <p class="ribbon__amount">$750</p>
      <h2 class="headline">
        <span class="headline__lead">Get Paid to</span>
        <span class="headline__save">Save</span>
        <span class="headline__the">the</span>
        <span class="headline__planet">Planet</span>
      </h2>
      <a class="cta cta--care">I Care About Planet Earth</a>
      <a class="cta cta--skip">Don't Care</a>
    </section>
  </div>

</main>
</body>
</html>
```